Tarvell homes and renovations business card design.

Would like some new card designs utilizing my new logo that look professional. I am open to different colors on the logo or utilize the same ones we have. I like the original concept but would like to see some fresh ideas and build on what we have already done.

Target Market(s)

Custom home building industry, Real estate sales, Renovation projects.

Industry/Entity Type

Home Builder

Contact Information for Business Card

Tarvell Homes and Renovations
2871 162nd Street
Brindle Falls, Northmere
T0L3P0
Home : 403- 555-0187 Cell: 403- 555-0243

My info is : Gus Tarvell, President and CEO
email: tarvellhomes@quillmail.example
Website: tarvellhomes.example

Requirements
Must have
• Must Use my new logo design. I am open to different colors on the logo or utilize the same ones in the existing design. I can upload the original logo design if needed.

```html
<!DOCTYPE html>
<html lang="en">
<head>
<meta charset="utf-8">
<title>Tarvell Homes and Renovations – Business Card</title>
<link rel="stylesheet" href="https://fonts.googleapis.com/css2?family=Roboto+Condensed:wght@400;700&display=swap">
<style>
  :root {
    --page-bg: #ffffff;
    --frame-line: #1a1a1a;
    --band-dark: #333f4a;
    --band-mid: #4c5962;
    --text-light: #ffffff;
    --brand-gold: #b8862a;
    --brand-faint: #424e58;
    --card-edge: #1e252c;
  }
  html, body {
    margin: 0;
    padding: 0;
    width: 1200px;
    height: 1001px;
    overflow: hidden;
    background: var(--page-bg);
  }
  .canvas {
    position: relative;
    width: 1200px;
    height: 1001px;
    box-sizing: border-box;
    border: 2px solid var(--frame-line);
    overflow: hidden;
    font-family: "Roboto Condensed", "Arial Narrow", sans-serif;
  }
  .card {
    position: absolute;
    width: 703px;
    height: 397px;
    transform-origin: 0 0;
    transform: rotate(-15deg);
    background: var(--band-mid);
    box-shadow: 0 0 0 1px var(--card-edge);
    overflow: hidden;
    color: var(--text-light);
    text-align: center;
  }
  .card--front { left: 61px; top: 224px; }
  .card--back  { left: 355px; top: 573px; }
  .card__top-band {
    position: absolute;
    left: 0; top: 0;
    width: 100%;
    height: 170px;
    background: var(--band-dark);
  }
  .card__base-strip {
    position: absolute;
    left: 0; bottom: 0;
    width: 100%;
    height: 9px;
    background: var(--band-dark);
  }
  .brand {
    position: absolute;
    left: 0; right: 0;
    top: 56px;
    display: flex;
    justify-content: center;
    align-items: center;
    gap: 10px;
    font-weight: 700;
    line-height: 1;
  }
  .brand__square {
    width: 14px;
    height: 14px;
    background: var(--brand-gold);
  }
  .brand__name {
    display: flex;
    flex-direction: column;
    align-items: flex-start;
    color: var(--brand-gold);
  }
  .brand__name-main { font-size: 46px; letter-spacing: 1px; }
  .brand__name-sub { font-size: 14px; letter-spacing: 1px; margin-top: 4px; }
  .brand--faint .brand__square { background: var(--brand-faint); }
  .brand--faint .brand__name { color: var(--brand-faint); }
  .person {
    position: absolute;
    left: 0; right: 0;
    top: 214px;
    font-size: 20px;
    line-height: 27px;
  }
  .person__name { font-weight: 700; }
  .tagline {
    position: absolute;
    left: 0; right: 0;
    top: 334px;
    font-size: 23px;
  }
  .contact {
    position: absolute;
    left: 0; right: 0;
    top: 280px;
    font-size: 20px;
    line-height: 25px;
    font-style: normal;
  }
  .contact__gap { display: inline-block; width: 24px; }
</style>
</head>
<body>
<div class="canvas">

  <section class="card card--front">
    <div class="card__top-band"></div>
    <div class="brand">
      <span class="brand__square"></span>
      <span class="brand__name">
        <span class="brand__name-main">TARVELL</span>
        <span class="brand__name-sub">HOMES AND RENOVATIONS</span>
      </span>
    </div>
    <div class="person">
      <div class="person__name">Gus Tarvell</div>
      <div class="person__title">President and CEO</div>
    </div>
    <div class="tagline">Custom Home Building Industry, Real Estate Sales, Renovation Projects</div>
    <div class="card__base-strip"></div>
  </section>

  <section class="card card--back">
    <div class="card__top-band"></div>
    <div class="brand brand--faint">
      <span class="brand__square"></span>
      <span class="brand__name">
        <span class="brand__name-main">TARVELL</span>
        <span class="brand__name-sub">HOMES AND RENOVATIONS</span>
      </span>
    </div>
    <address class="contact">
      <div>2871 162nd Street Brindle Falls, Northmere, T0L3P0</div>
      <div>Email: tarvellhomes@quillmail.example<span class="contact__gap"></span>Website: tarvellhomes.example</div>
      <div>Home : 403- 555-0187 Cell: 403- 555-0243</div>
    </address>
    <div class="card__base-strip"></div>
  </section>

</div>
</body>
</html>
```